Fernhollow Co Website Design

We are working with a water product retailer in Washington called Fernhollow Co.

Some sites to use for content/competitors and inspiration:

https://www.brivelto.com
https://tanmoril.example/designs/retail/ (lots of retail website designs we've approved and continue to show clients)

Thank you for taking the time to consider designing a website for us. We are web developers based in Stockton, CA, USA. Most of our projects go through the same process. Understanding this process may help you win a project with us. We custom-code all of our websites in-house. We don’t have any requirements as to what tools you use for your design, but we prefer Figma files. For any design that we label as four-stars, we send it to the client for review. The client picks the final design they want us to use. Once we complete this process, we will continue to show additional clients all the four-star sites and purchase them later. Your designs will have multiple chances to sell. For better chances of success, we ask that you follow these guidelines.

IMAGES:
If you use any images or icons in the design, we ask that you have a link to the asset so we can purchase the image/icon. Most of the designs we submit do not have the customer’s images on them unless they have some great images. Be creative; show us the feeling you are trying to portray with your image choices. Use any royalty-free site you choose. We subscribe to Varnex and mainly use their images, but we can purchase images outside of Varnex.

PLEASE NOTE: we will not submit designs to clients with watermarks on the images.

FONTS:
We ask that you identify the fonts used in the design. This can be done in a message if you want. We typically use Google Fonts and Varnex Fonts.

CONTENT:
We're always open to different content and ideas. We often submit designs with stock images so the client can see our vision. We typically take pictures after the website launch to use their images with our vision. Lorem Ipsum is fine for paragraphs, but we ask that you write the headers in correct English. We want to be able to show the vision and identify the sections of the website.

INSPIRATION:
We typically add a couple of links in the brief of websites we like to help you get started in your design.

REVISIONS:
We do not often ask for revisions of the designs unless we see something in the design that may not appeal to the client. If there are slight changes that we want to make, we do that in the development process.

FEEDBACK:
We rarely give feedback on designs during the design process. We are working on many website projects and do not have the time to provide feedback. We usually respond if your request is well thought out and asks specific questions, but a note asking “feedback, please” usually goes unanswered.

```html
<!DOCTYPE html>
<html lang="en">
<head>
<meta charset="utf-8">
<title>Fernhollow Co — Home</title>
<link href="https://fonts.googleapis.com/css2?family=Gilda+Display&family=Roboto:ital,wght@0,400;0,500;0,700;1,400&display=swap" rel="stylesheet">
<style>
:root{
  --brand:#1d80ad;
  --brand-deep:#1b8cbd;
  --pink:#ff0a84;
  --ink:#111;
  --text:#555;
  --white:#fff;
  --star:#f0a23a;
}
*{box-sizing:border-box;margin:0;padding:0}
html,body{width:1200px;height:3822px;overflow:hidden}
body{position:relative;font-family:"Roboto",sans-serif;color:var(--text);background:var(--white)}
.abs{position:absolute}
.btn{position:absolute;display:flex;align-items:center;justify-content:center;background:var(--pink);color:var(--white);font:700 14px "Roboto",sans-serif;border-radius:22px;text-transform:uppercase}
.section-title{position:absolute;left:0;width:1200px;text-align:center;color:var(--brand);font-family:"Gilda Display",serif;font-weight:400;font-size:46px;line-height:54px;letter-spacing:2px;text-transform:uppercase}
.body-copy{font-size:15.5px;line-height:26px;color:var(--text)}
.photo{position:absolute}

.topbar{left:0;top:0;width:1200px;height:30px;background:var(--brand-deep);color:var(--white);font-size:12px;text-align:center;line-height:30px}

.hero{left:0;top:30px;width:1200px;height:510px;background:linear-gradient(90deg,#e8f7fd 0%,#d4f1fc 45%,#bfeafb 80%,#c9eefc 100%)}
.hero-art{left:0;top:60px;width:680px;height:480px;background:radial-gradient(ellipse at 42% 45%,#4d8fdc 0%,#8cc6f0 35%,rgba(200,236,251,0) 70%)}
.logo{left:111px;top:42px;color:var(--brand);font-family:"Gilda Display",serif;font-size:26px;line-height:32px}
.nav{left:310px;top:56px;display:flex;gap:34px;font-size:13.5px;font-weight:700;color:var(--ink)}
.nav .active{color:var(--pink)}
.nav-icons{left:862px;top:52px;display:flex;gap:16px}
.search{left:973px;top:40px;width:116px;height:42px;border-radius:21px;gap:6px}
.hero-copy{left:640px;top:180px;width:490px;text-align:center}
.hero-copy .kicker{font-size:26px;color:var(--ink);line-height:32px}
.hero-copy h1{font-family:"Gilda Display",serif;font-weight:400;color:var(--brand);font-size:48px;letter-spacing:2px;line-height:60px;text-transform:uppercase;white-space:nowrap}
.hero-copy p{font-size:15.5px;line-height:26px;color:#222;margin-top:8px}

.feature-title{color:var(--brand);font-family:"Gilda Display",serif;font-weight:400;font-size:44px;line-height:50px;letter-spacing:2px;text-transform:uppercase}

.habit-band{left:0;top:1953px;width:1200px;height:473px;background:linear-gradient(90deg,#4e94cf 0%,#86c2ea 30%,#c9e9f8 55%,#d8f0fb 75%,#bfe3f5 100%)}
.habit-title{left:600px;top:2000px;font-family:"Gilda Display",serif;font-weight:400;color:var(--ink);font-size:44px;line-height:49px}

.card{position:absolute;top:2594px;width:309px;height:253px;background:var(--white);box-shadow:0 2px 10px rgba(0,0,0,.12);text-align:center;padding-top:30px}
.card .stars{display:flex;justify-content:center;gap:8px}
.card p{font-style:italic;font-size:15px;line-height:26px;color:#555;padding:14px 18px 0}
.card .name{color:var(--brand);font-weight:700;font-size:20px;margin-top:8px}
.arrow{position:absolute;top:2690px;width:34px;height:34px}

.newsletter{left:0;top:3292px;width:1200px;height:178px;background:var(--brand-deep)}
.news-input{left:311px;top:3396px;width:585px;height:50px;border-radius:25px;background:var(--white);color:#999;font-size:15px;line-height:50px;padding-left:15px}
.subscribe{left:766px;top:3401px;width:126px;height:40px;font-size:15px}

.footer{left:0;top:3470px;width:1200px;height:352px;background:var(--brand-deep);color:var(--white)}
.footer .rule{position:absolute;background:rgba(255,255,255,.6)}
.footer h4{position:absolute;font-weight:700;font-size:20px}
.footer .link{position:absolute;left:408px;font-weight:700;font-size:13.5px}
.contact-icon{position:absolute;left:604px;width:42px;height:42px;border-radius:50%;background:var(--white);display:flex;align-items:center;justify-content:center}
.contact-text{position:absolute;left:662px;font-size:15.5px;line-height:21px}
.social{position:absolute;top:66px;width:38px;height:38px;border-radius:50%;border:1.5px solid var(--white)}
</style>
</head>
<body>

<div class="abs topbar">FREE SHIPPING OVER $65</div>

<header>
  <div class="abs hero"></div>
  <div class="photo hero-art" role="img" aria-label="Blue water bottle bursting through a splash of clear water"></div>
  <svg class="abs" style="left:0;top:470px" width="1200" height="70" viewBox="0 0 1200 70"><path d="M0 60 C80 20 160 35 240 48 C330 60 420 40 520 30 C620 22 700 45 800 40 C900 35 960 10 1040 18 C1110 25 1160 45 1200 55 L1200 70 L0 70 Z" fill="#fff"/></svg>

  <div class="abs logo">Fernhollow Co</div>

  <nav class="abs nav">
    <span class="active">HOME</span><span>ABOUT US</span><span>PRODUCTS</span><span>TESTIMONIALS</span><span>CONTACT US</span>
  </nav>
  <div class="abs nav-icons">
    <svg width="16" height="16" viewBox="0 0 16 16"><circle cx="8" cy="5" r="3.5" fill="#111"/><path d="M1.5 16 C1.5 10 14.5 10 14.5 16 Z" fill="#111"/></svg>
    <svg width="18" height="16" viewBox="0 0 18 16"><path d="M9 15 L2 8 C-1 4 3 -1 9 4 C15 -1 19 4 16 8 Z" fill="#111"/></svg>
    <svg width="16" height="16" viewBox="0 0 16 16"><path d="M5 5 V3.5 C5 0.5 11 0.5 11 3.5 V5" stroke="#111" stroke-width="1.6" fill="none"/><rect x="1.5" y="5" width="13" height="10.5" rx="2" fill="#111"/></svg>
  </div>
  <div class="btn search"><svg width="15" height="15" viewBox="0 0 15 15"><circle cx="6" cy="6" r="4.6" stroke="#fff" stroke-width="2" fill="none"/><path d="M9.5 9.5 L14 14" stroke="#fff" stroke-width="2.2"/></svg>SEARCH</div>

  <div class="abs hero-copy">
    <div class="kicker">WELCOME TO</div>
    <h1>Fernhollow Co</h1>
    <p>Lorem ipsum dolor sit amet, consectetur ipiscing elit,<br>sed do eiusmod tempor.</p>
  </div>
  <div class="btn" style="left:827px;top:348px;width:115px;height:40px">SHOP NOW</div>
</header>

<section>
  <h2 class="section-title" style="top:612px">About Us</h2>
  <p class="abs body-copy" style="left:195px;top:687px;width:810px;text-align:center">Lorem ipsum dolor sit amet, consectetur adipiscing elit, sed do eiusmod tempor incididunt ut labore et dolore magna aliqua. Ut enim ad minim veniam, quis nostrud exercitation ullamco laboris nisi ut aliquip ex ea commodo consequat. Duis aute irure dolor in reprehenderit in voluptate velit esse cillum dolore eu fugiat nulla pariatur. Excepteur sint occaecat cupidatat non proident, sunt in culpa qui officia deserunt mollit anim id est laborum.</p>
  <div class="btn" style="left:543px;top:805px;width:114px;height:42px">READ MORE</div>
</section>

<section>
  <div class="photo" style="left:0;top:934px;width:556px;height:422px;background:linear-gradient(160deg,#9dbcb2 0%,#5d7a56 40%,#3a4636 75%,#2a3026 100%)" role="img" aria-label="Glass of clear water on a rock beside a mountain stream"></div>
  <h2 class="abs feature-title" style="left:644px;top:922px;width:500px">Hack Lunch With Quick, Complete Nutrition</h2>
  <p class="abs body-copy" style="left:644px;top:1097px;width:450px">Lorem ipsum dolor sit amet, consectetur adipiscing elit, sed do eiusmod tempor incididunt ut labore et dolore magna aliqua. uis ipsum suspendisse ultrices gravida. Risus commodo viverra enas accumsan lacus vel facilisis.Lorem ipsum dolor sit amet, ectetur adipiscing elit, sed do eiusmod tempor incididunt ut labore et lore magna aliqua. uis ipsum suspendisse ultrices gravida. Risus odo viverra enas accumsan lacus vel facilisis.</p>
  <div class="btn" style="left:644px;top:1296px;width:115px;height:42px">READ MORE</div>
</section>

<section>
  <h2 class="abs feature-title" style="left:111px;top:1433px;width:460px">Chosen By Top Performers</h2>
  <p class="abs body-copy" style="left:111px;top:1560px;width:450px">Lorem ipsum dolor sit amet, consectetur adipiscing elit, sed do d tempor incididunt ut labore et dolore magna aliqua. uis ipsum se ultrices gravida. Risus commodo viverra enas ccumsan lacus vel facilisis.Lorem ipsum dolor sit amet, ectetur adipiscing elit, sed do eiusmod tempor incididunt ut labore et lore magna aliqua. uis ipsum suspendisse ultrices gravida. Risus odo viverra enas msan lacus vel facilisis labore et lore magna aliqua.</p>
  <p class="abs body-copy" style="left:111px;top:1752px;width:450px">Lorem ipsum dolor sit amet, consectetur adipiscing elit, sed doh tempor incididunt ut labore et dolore magna aliqua.</p>
  <div class="btn" style="left:111px;top:1814px;width:116px;height:42px">READ MORE</div>
  <div class="photo" style="left:642px;top:1444px;width:558px;height:419px;background:linear-gradient(135deg,#d3cc8a 0%,#86a458 35%,#4f7a3c 65%,#2f4f26 100%)" role="img" aria-label="Hand pouring bottled water into a glass outdoors"></div>
</section>

<section>
  <div class="photo habit-band" role="img" aria-label="Water bottle splashing into rippling blue water"></div>
  <h2 class="abs habit-title">The Healthy Habit<br>That Saves</h2>
  <p class="abs body-copy" style="left:600px;top:2121px;width:495px;color:#444">Lorem ipsum dolor sit amet, consectetur adipiscing elit, sed do d empor incididunt ut labore et dolore magna aliqua. uis ipsum se ultrices avida. Risus commodo viverra enas ccumsan lacus vel facilisis.Lorem ipsum dolor sit amet, ectetur adipiscing elit, sed do eiusmod tempor incididunt ut labore et lore magna aliqua. uis ipsum suspendisse ultrices gravida. Risus odo viverra enas msan lacus vel facilisis labore et lore magna aliqua ipsum suspendisse ultrices gravida.</p>
  <div class="btn" style="left:600px;top:2314px;width:116px;height:42px">READ MORE</div>
</section>

<section>
  <h2 class="section-title" style="top:2502px">Client Testimonials</h2>
  <svg class="arrow" style="left:39px" viewBox="0 0 34 34"><circle cx="17" cy="17" r="17" fill="#1d80ad"/><path d="M19.5 10.5 L13 17 L19.5 23.5" stroke="#fff" stroke-width="2.4" fill="none"/></svg>
  <svg class="arrow" style="left:1125px" viewBox="0 0 34 34"><circle cx="17" cy="17" r="16" fill="#fff" stroke="#1d80ad" stroke-width="1.5"/><path d="M14.5 10.5 L21 17 L14.5 23.5" stroke="#1d80ad" stroke-width="2" fill="none"/></svg>

  <div class="card" style="left:111px">
    <div class="stars">
      <svg width="22" height="21" viewBox="0 0 22 21"><path d="M11 0 L13.6 7.6 L21.6 7.8 L15.2 12.6 L17.6 20.4 L11 15.8 L4.4 20.4 L6.8 12.6 L0.4 7.8 L8.4 7.6 Z" fill="#f0a23a"/></svg>
      <svg width="22" height="21" viewBox="0 0 22 21"><path d="M11 0 L13.6 7.6 L21.6 7.8 L15.2 12.6 L17.6 20.4 L11 15.8 L4.4 20.4 L6.8 12.6 L0.4 7.8 L8.4 7.6 Z" fill="#f0a23a"/></svg>
      <svg width="22" height="21" viewBox="0 0 22 21"><path d="M11 0 L13.6 7.6 L21.6 7.8 L15.2 12.6 L17.6 20.4 L11 15.8 L4.4 20.4 L6.8 12.6 L0.4 7.8 L8.4 7.6 Z" fill="#f0a23a"/></svg>
      <svg width="22" height="21" viewBox="0 0 22 21"><path d="M11 0 L13.6 7.6 L21.6 7.8 L15.2 12.6 L17.6 20.4 L11 15.8 L4.4 20.4 L6.8 12.6 L0.4 7.8 L8.4 7.6 Z" fill="#f0a23a"/></svg>
      <svg width="22" height="21" viewBox="0 0 22 21"><path d="M11 0 L13.6 7.6 L21.6 7.8 L15.2 12.6 L17.6 20.4 L11 15.8 L4.4 20.4 L6.8 12.6 L0.4 7.8 L8.4 7.6 Z" fill="#f0a23a"/></svg>
    </div>
    <p>“Lorem ipsum dolor sit amet, onsectetur adipiscing elit, sed do eiusmod tempor incididunt ut labore et dolore magna aliqua. Quis ipsum suspendisse ultrices gravida.”</p>
    <div class="name">-ROBORT</div>
  </div>
  <div class="card" style="left:446px">
    <div class="stars">
      <svg width="22" height="21" viewBox="0 0 22 21"><path d="M11 0 L13.6 7.6 L21.6 7.8 L15.2 12.6 L17.6 20.4 L11 15.8 L4.4 20.4 L6.8 12.6 L0.4 7.8 L8.4 7.6 Z" fill="#f0a23a"/></svg>
      <svg width="22" height="21" viewBox="0 0 22 21"><path d="M11 0 L13.6 7.6 L21.6 7.8 L15.2 12.6 L17.6 20.4 L11 15.8 L4.4 20.4 L6.8 12.6 L0.4 7.8 L8.4 7.6 Z" fill="#f0a23a"/></svg>
      <svg width="22" height="21" viewBox="0 0 22 21"><path d="M11 0 L13.6 7.6 L21.6 7.8 L15.2 12.6 L17.6 20.4 L11 15.8 L4.4 20.4 L6.8 12.6 L0.4 7.8 L8.4 7.6 Z" fill="#f0a23a"/></svg>
      <svg width="22" height="21" viewBox="0 0 22 21"><path d="M11 0 L13.6 7.6 L21.6 7.8 L15.2 12.6 L17.6 20.4 L11 15.8 L4.4 20.4 L6.8 12.6 L0.4 7.8 L8.4 7.6 Z" fill="#f0a23a"/></svg>
      <svg width="22" height="21" viewBox="0 0 22 21"><path d="M11 0 L13.6 7.6 L21.6 7.8 L15.2 12.6 L17.6 20.4 L11 15.8 L4.4 20.4 L6.8 12.6 L0.4 7.8 L8.4 7.6 Z" fill="#f0a23a"/></svg>
    </div>
    <p>“Lorem ipsum dolor sit amet, onsectetur adipiscing elit, sed do eiusmod tempor incididunt ut labore et dolore magna aliqua. Quis ipsum suspendisse ultrices gravida.”</p>
    <div class="name">-WILLIAM</div>
  </div>
  <div class="card" style="left:780px">
    <div class="stars">
      <svg width="22" height="21" viewBox="0 0 22 21"><path d="M11 0 L13.6 7.6 L21.6 7.8 L15.2 12.6 L17.6 20.4 L11 15.8 L4.4 20.4 L6.8 12.6 L0.4 7.8 L8.4 7.6 Z" fill="#f0a23a"/></svg>
      <svg width="22" height="21" viewBox="0 0 22 21"><path d="M11 0 L13.6 7.6 L21.6 7.8 L15.2 12.6 L17.6 20.4 L11 15.8 L4.4 20.4 L6.8 12.6 L0.4 7.8 L8.4 7.6 Z" fill="#f0a23a"/></svg>
      <svg width="22" height="21" viewBox="0 0 22 21"><path d="M11 0 L13.6 7.6 L21.6 7.8 L15.2 12.6 L17.6 20.4 L11 15.8 L4.4 20.4 L6.8 12.6 L0.4 7.8 L8.4 7.6 Z" fill="#f0a23a"/></svg>
      <svg width="22" height="21" viewBox="0 0 22 21"><path d="M11 0 L13.6 7.6 L21.6 7.8 L15.2 12.6 L17.6 20.4 L11 15.8 L4.4 20.4 L6.8 12.6 L0.4 7.8 L8.4 7.6 Z" fill="#f0a23a"/></svg>
      <svg width="22" height="21" viewBox="0 0 22 21"><path d="M11 0 L13.6 7.6 L21.6 7.8 L15.2 12.6 L17.6 20.4 L11 15.8 L4.4 20.4 L6.8 12.6 L0.4 7.8 L8.4 7.6 Z" fill="#f0a23a"/></svg>
    </div>
    <p>“Lorem ipsum dolor sit amet, onsectetur adipiscing elit, sed do eiusmod tempor incididunt ut labore et dolore magna aliqua. Quis ipsum suspendisse ultrices gravida.”</p>
    <div class="name">-JHONSON</div>
  </div>
</section>

<section>
  <div class="photo" style="left:0;top:2936px;width:222px;height:356px;background:linear-gradient(180deg,#dcd8d3,#a8988a 55%,#3c3f52)" role="img" aria-label="Woman drinking a glass of water"></div>
  <div class="photo" style="left:230px;top:2936px;width:240px;height:356px;background:linear-gradient(180deg,#6ab9d3,#55a9c6 60%,#6cbdcc)" role="img" aria-label="Woman drinking from a bottle"></div>
  <div class="photo" style="left:479px;top:2936px;width:240px;height:356px;background:linear-gradient(180deg,#b3c0c9,#dcc1a6 45%,#2a88cc 80%)" role="img" aria-label="Runner drinking from a water bottle"></div>
  <div class="photo" style="left:727px;top:2936px;width:240px;height:356px;background:linear-gradient(180deg,#cfd7dc,#6a4d40 50%,#b06a5c)" role="img" aria-label="Smiling woman drinking from a sports bottle"></div>
  <div class="photo" style="left:976px;top:2936px;width:224px;height:356px;background:linear-gradient(180deg,#b0d6f0,#97796a 50%,#2a2e33)" role="img" aria-label="Man drinking from a water bottle outdoors"></div>
</section>

<section>
  <div class="abs newsletter"></div>
  <h2 class="section-title" style="top:3326px;color:#fff">Our Newsletter</h2>
  <div class="abs news-input">Enter Email Here</div>
  <div class="btn subscribe">SUBSCRIBE</div>
</section>

<footer class="abs footer">
  <div class="rule" style="left:0;top:0;width:1200px;height:1px"></div>
  <div class="rule" style="left:353px;top:0;width:1px;height:296px"></div>
  <div class="rule" style="left:568px;top:0;width:1px;height:296px"></div>
  <div class="rule" style="left:903px;top:0;width:1px;height:296px"></div>
  <div class="rule" style="left:0;top:296px;width:1200px;height:1px"></div>

  <div class="abs" style="left:111px;top:42px;font-family:'Gilda Display',serif;font-size:36px;line-height:46px;color:#fff">Fernhollow Co</div>
  <p class="abs" style="left:111px;top:130px;width:235px;font-size:15.5px;line-height:26px">Lorem ipsum dolor sit amet, tetur adipiscing elit, sed do eiusmod tempor incididunt ut labore et dolore facilisis.</p>

  <h4 style="left:405px;top:42px">QUICK LINKS</h4>
  <div class="link" style="top:94px">HOME</div>
  <div class="link" style="top:134px">ABOUT US</div>
  <div class="link" style="top:174px">PRODUCTS</div>
  <div class="link" style="top:214px">TESTIMONIALS</div>
  <div class="link" style="top:255px">CONTACT US</div>

  <h4 style="left:604px;top:42px">CONTACT US</h4>
  <div class="contact-icon" style="top:79px"><svg width="18" height="18" viewBox="0 0 18 18"><path d="M4 1 L7 5 L5.5 7 C6.5 9.5 8.5 11.5 11 12.5 L13 11 L17 14 L15 17 C8 17 1 10 1 3 Z" fill="#1b8cbd"/></svg></div>
  <div class="contact-text" style="top:79px"><b>PHONE NO:</b><br>+(555) 014 2290</div>
  <div class="contact-icon" style="top:142px"><svg width="18" height="14" viewBox="0 0 18 14"><rect x="0" y="0" width="18" height="14" rx="2" fill="#1b8cbd"/><path d="M1 1.5 L9 8 L17 1.5" stroke="#fff" stroke-width="1.6" fill="none"/></svg></div>
  <div class="contact-text" style="top:142px;left:666px"><b>EMAIL:</b><br>hello@fernhollowco.example</div>
  <div class="contact-icon" style="top:206px"><svg width="16" height="20" viewBox="0 0 16 20"><path d="M8 0 C3.5 0 0 3.4 0 7.8 C0 13 8 20 8 20 C8 20 16 13 16 7.8 C16 3.4 12.5 0 8 0 Z" fill="#1b8cbd"/><circle cx="8" cy="7.8" r="3" fill="#fff"/></svg></div>
  <div class="contact-text" style="top:202px;left:665px"><b>LOCATION:</b><br>Lorem ipsum dolor sit amet,<br>nsectetur adipiscing,USA</div>

  <h4 style="left:940px;top:42px">FOLLOW US</h4>
  <div class="social" style="left:946px;background:#fff" aria-label="Social profile one"></div>
  <div class="social" style="left:1000px" aria-label="Social profile two"></div>
  <div class="social" style="left:1053px" aria-label="Social profile three"></div>

  <div class="abs" style="left:0;top:312px;width:1200px;text-align:center;font-size:15.5px">Copyright © 2024 Fernhollow Co | All Rights Reserved</div>
</footer>

</body>
</html>
```